Annual accounts report for clients accountancyfirm

We require the design of a report template (front page and divider pages) of annual accounts for our clients. It is important that this report is professional and has some graphical elements. Please use our corporate colours and on the front page a blank rectangle to incorporate the data of the client (name, address, etc)

Target Market(s)

Professional clients of an accountancy firm

Industry/Entity Type

Accountant

Font styles to use
Sans Serif

Colors
f04a50
ec1f27
ffffff
f68e4e

Requirements
Must have
• Must be higly distinctive and professional
Nice to have
• some creative elements
Should not have
• a lot of text

```html
<!DOCTYPE html>
<html lang="en">
<head>
<meta charset="UTF-8">
<title>Annual Report 2020 – Pellbrook Partners</title>
<link rel="stylesheet" href="https://fonts.googleapis.com/css2?family=Archivo+Black&display=swap">
<style>
  :root {
    --brand-red: #a61c24;
    --accent-red: #ec1f27;
    --paper: #ffffff;
    --network-grey: #e9e7e8;
    --network-rose: #f6e3e4;
  }
  html, body {
    margin: 0;
    padding: 0;
    overflow: hidden;
    background: var(--paper);
  }
  .cover {
    position: relative;
    width: 849px;
    height: 1200px;
    overflow: hidden;
    background: var(--paper);
    font-family: "Archivo Black", sans-serif;
    color: var(--brand-red);
  }
  .brand {
    position: absolute;
    top: 30px;
    right: 40px;
    display: flex;
    align-items: center;
    gap: 8px;
  }
  .brand-mark {
    width: 10px;
    height: 10px;
    border: 2px solid var(--brand-red);
  }
  .brand-name {
    font-size: 16px;
    line-height: 1.15;
    letter-spacing: 1px;
    color: var(--brand-red);
  }
  .title-annual {
    position: absolute;
    left: 40px;
    top: 56px;
    margin: 0;
    font-size: 40px;
    font-weight: 400;
    line-height: 1;
    letter-spacing: 18px;
  }
  .title-report {
    position: absolute;
    left: 38px;
    top: 86px;
    margin: 0;
    font-size: 80px;
    line-height: 1;
    letter-spacing: -3px;
  }
  .title-rule {
    position: absolute;
    left: 38px;
    top: 174px;
  }
  .rule-line {
    stroke: var(--accent-red);
    stroke-width: 2.5;
  }
  .rule-end {
    fill: var(--paper);
    stroke: var(--brand-red);
    stroke-width: 1.5;
  }
  .title-year {
    position: absolute;
    left: 186px;
    top: 190px;
    margin: 0;
    font-size: 38px;
    line-height: 1;
    letter-spacing: 20px;
  }
  .client-box {
    position: absolute;
    left: 40px;
    top: 310px;
    width: 545px;
    height: 256px;
    border: 1.5px solid var(--brand-red);
  }
  .network {
    position: absolute;
    left: 0;
    top: 0;
  }
  .network-stop-a { stop-color: var(--network-grey); }
  .network-stop-b { stop-color: var(--network-rose); }
</style>
</head>
<body>
  <main class="cover">
    <div class="brand">
      <span class="brand-mark"></span>
      <span class="brand-name">PELLBROOK<br>PARTNERS</span>
    </div>

    <h1 class="title-annual">Annual</h1>
    <p class="title-report">Report</p>

    <svg class="title-rule" width="480" height="16" viewBox="0 0 480 16">
      <line class="rule-line" x1="0" y1="7.5" x2="447" y2="7.5"/>
      <circle class="rule-end" cx="458" cy="7.5" r="10.5"/>
    </svg>

    <p class="title-year">2020</p>

    <div class="client-box" aria-label="Client details area"></div>

    <svg class="network" width="849" height="1200" viewBox="0 0 849 1200" role="img"
         aria-label="Connected network of red and grey lines with nodes spreading across the lower page">
      <defs>
        <linearGradient id="network-fill" x1="0" y1="0" x2="1" y2="1">
          <stop class="network-stop-a" offset="0"/>
          <stop class="network-stop-b" offset="1"/>
        </linearGradient>
      </defs>
      <polygon fill="url(#network-fill)"
               points="14,662 60,672 215,738 496,600 556,722 572,612 792,476 838,486 838,1200 14,1200"/>
    </svg>
  </main>
</body>
</html>
```